Professional Consulting Firm Business Card Design

We need a business card design for a new professional consulting firm that specializes in petroleum, health, and financial consulting. We need a design that is trendy but elegant, and one that would make a vantage 300 executive feel comfortable using our services. I have attached a logo that needs to be used in the design. I have also attached a photo of a card design that I like.

On the card we need a place for employee name, title, email address, fax number, phone number, mailing address, and website address.

Industry/Entity Type

Financial

Contact Information for Business Card

see attached

Font styles to use
Other font styles liked:
• Calibri or your choice

Requirements
Must have
• style
Nice to have
• texture, rounded edges
Should not have
• no solid black cards but black may be used

```html
<!DOCTYPE html>
<html lang="en">
<head>
<meta charset="utf-8">
<title>Ridgeline Advisory – Business Card</title>
<link href="https://fonts.googleapis.com/css2?family=Mulish:wght@400;700&display=swap" rel="stylesheet">
<style>
  :root {
    --backdrop: #e9e6e2;
    --card: #ffffff;
    --brand-blue: #1d4a85;
    --ink: #4a4a4a;
    --ink-soft: #555555;
  }
  * { margin: 0; padding: 0; box-sizing: border-box; }
  html, body {
    width: 1200px; height: 894px; overflow: hidden;
    background: var(--backdrop);
    font-family: "Mulish", sans-serif;
  }
  .business-card {
    position: absolute;
    left: 234px; top: 237px;
    width: 727px; height: 427px;
    background: var(--card);
    box-shadow: 0 4px 14px rgba(0,0,0,0.18);
  }
  .brand {
    position: absolute; left: 36px; top: 46px;
  }
  .brand-name {
    font-size: 40px; font-weight: 400; letter-spacing: -0.5px;
    color: var(--ink); line-height: 1;
  }
  .brand-tagline {
    margin-top: 8px;
    font-size: 10px; font-weight: 700; letter-spacing: 0.2px;
    color: var(--brand-blue); text-transform: uppercase;
  }
  .person {
    position: absolute; left: 36px; top: 243px;
  }
  .person-name {
    font-size: 20px; font-weight: 700; color: var(--brand-blue); line-height: 24px;
  }
  .person-title {
    font-size: 16.5px; color: var(--ink-soft); line-height: 22px;
  }
  .contact {
    position: absolute; left: 452px; top: 242px;
    color: var(--ink-soft); font-size: 16.5px; line-height: 21px;
  }
  .contact-address { margin-bottom: 8px; }
  .contact-list { list-style: none; }
  .contact-list li { display: flex; align-items: center; gap: 8px; }
  .contact-list svg { width: 14px; height: 14px; fill: var(--brand-blue); flex: none; }
</style>
</head>
<body>
  <section class="business-card">
    <header class="brand">
      <div class="brand-name">Ridgeline Advisory</div>
      <div class="brand-tagline">Health, Safety, and Financial Consulting Services</div>
    </header>

    <div class="person">
      <div class="person-name">Daniel R. Whitmore</div>
      <div class="person-title">Managing Director</div>
    </div>

    <div class="contact">
      <address class="contact-address" style="font-style:normal">
        410 Larkspur Ave., Ste. 1200 North<br>
        Aurelia Colorado 80415
      </address>
      <ul class="contact-list">
        <li>
          <svg viewBox="0 0 16 16" aria-hidden="true"><path d="M4 1l3 3-2 2c1 2 3 4 5 5l2-2 3 3-2 3C7 15 1 9 1 3z"/></svg>
          + 999 999 9999
        </li>
        <li>
          <svg viewBox="0 0 16 16" aria-hidden="true"><path d="M1 5c0-2 14-2 14 0v1h-4V5H5v1H1z"/><rect x="3" y="7" width="10" height="7" rx="1"/></svg>
          + 999 999 9999
        </li>
        <li>
          <svg viewBox="0 0 16 16" aria-hidden="true"><rect x="4" y="1" width="8" height="4"/><rect x="1" y="6" width="14" height="6" rx="1"/><rect x="4" y="10" width="8" height="5"/></svg>
          + 999 999 9999
        </li>
        <li>
          <svg viewBox="0 0 16 16" aria-hidden="true"><path d="M1 3h14v10H1z M2 4l6 5 6-5" stroke="#fff" stroke-width="1"/></svg>
          info@ridgelineadvisory.com
        </li>
        <li>
          <svg viewBox="0 0 16 16" aria-hidden="true"><circle cx="8" cy="8" r="7"/><path d="M1 8h14M8 1c-3 4-3 10 0 14M8 1c3 4 3 10 0 14" stroke="#fff" stroke-width="1" fill="none"/></svg>
          www.ridgelineadvisory.com
        </li>
      </ul>
    </div>
  </section>
</body>
</html>
```